【概要】 求人サイトに掲載するサムネイル画像作成依頼です。 素敵なデザインがあれば複数採用いたします。 【 依頼内容 】 ・サイズ:横900x縦600 ・ターゲット:20代~50代向けの求人 【 入れていただきたい文言】※これ以外の文言は入れないでください ・固定ルート+体力負担なし+無理な運転はさせない社風=長く働ける環境です! ・6tドライバー募集 ・月給35万円可能 【画像に関して】 注:こちらの画像サイズ、データで提出できる方のみお願い致します。 ★「横900ピクセルx縦600ピクセル」(PNGファイル×1、PSDデータ×1) ・配信時は制作したバナーがスマホの画面幅程度に縮小されて表示されます。テキストの可読性を考慮して制作お願いします。 ・文字を記入する際、できれば画像としてではなく、フォトショップのテキストを使用していただければと存じます。 ・テキストデータはアウトライン化されていない、後から編集できる状態での納品をお願いいたします。(イラストレーターNG) ・フォントやあしらいにフリー素材を使用する場合は著作権に抵触しないものをご利用下さい。 【重要な指定】 ※目を惹きクリックされるインパクトのあるバナーをお願い致します。 サイト内で使用するものなので「こちらをクリック」「詳細はこちら」などのフレーズはなしでお願いいたします。 ・添付画像をご使用ください ・添付画像は反転しないで下さい 【ご注意】 ※他で登録されているデザインや商標の転用など、他社の知的財産権を侵すことNG ※他のクライアントへ既に提案した内容の転用などNG ※ご提案頂きましたバナー案について、SNSへの投稿・Webサイトへのアップ等NG →ポートフォリオ・コンペ提案作品一覧にもアップNGです。 アップする際には、社名を削除し、写真はフリー素材に差し替えてください。 ※今後、画像を再利用する可能性がございます。 ※WEBサイトで他の求人に使用することがあります。 【対応時間】 平日:9時半~18時半 その他ご質問、ご不明点等ありましたら、気軽にお問い合わせください。 見やすく、素敵なデザインをお待ちしております! |
どの案も素敵でしたが、こちらの作品が一番イメージに合っておりました。
皆様ご提案ありがとうございました。どれも個性的でよい提案ばかりでした。また機会がありましたら依頼させていただきますのでよろしくお願いします。

```html
<!DOCTYPE html>
<html lang="ja">
<head>
<meta charset="utf-8">
<title>6tドライバー募集</title>
<link href="https://fonts.googleapis.com/css2?family=Noto+Sans+JP:wght@700;900&display=swap" rel="stylesheet">
<style>
  :root{
    --yellow:#f6d21a;
    --red:#e8281e;
    --white:#ffffff;
    --ink:#1a1a1a;
    --blue-top:#38b6f0;
    --blue-bottom:#1a3fa8;
    --photo-dark:#2c3a5c;
    --photo-light:#c9c2b0;
    --truck:#e9ecef;
  }
  html,body{margin:0;padding:0;overflow:hidden;}
  body{width:1200px;height:800px;font-family:"Noto Sans JP",sans-serif;}
  .banner{position:relative;width:1200px;height:800px;background:var(--yellow);overflow:hidden;}
  .decor{position:absolute;left:0;top:0;}
  .photo{position:absolute;}
  .photo--crew{left:250px;top:170px;width:650px;height:630px;
    background:linear-gradient(180deg,var(--photo-light) 0%,var(--photo-dark) 40%,#1f2a44 100%);
    border-radius:200px 200px 0 0;}
  .photo--truck-left{left:0;top:0;width:275px;height:275px;
    background:linear-gradient(180deg,var(--truck),#b8bec6);border-radius:0 0 24px 0;}
  .photo--truck-right{left:940px;top:0;width:260px;height:240px;
    background:linear-gradient(180deg,var(--truck),#b8bec6);border-radius:0 0 0 24px;}
  .headline{position:absolute;left:300px;top:54px;width:610px;height:86px;background:var(--white);
    display:flex;align-items:center;justify-content:center;
    color:var(--red);font-weight:900;font-size:60px;letter-spacing:1px;margin:0;}
  .salary-label,.salary-unit{position:absolute;margin:0;color:var(--red);font-weight:900;line-height:1;
    text-shadow:3px 0 0 var(--white),-3px 0 0 var(--white),0 3px 0 var(--white),0 -3px 0 var(--white),
      2px 2px 0 var(--white),-2px -2px 0 var(--white),2px -2px 0 var(--white),-2px 2px 0 var(--white);}
  .salary-label{left:38px;top:296px;font-size:82px;}
  .salary-unit{left:150px;top:640px;font-size:84px;}
  .salary-figure{position:absolute;left:58px;top:372px;}
  .points{position:absolute;left:808px;top:282px;width:344px;margin:0;padding:0;list-style:none;
    display:flex;flex-direction:column;align-items:center;}
  .points__item{width:100%;background:var(--white);color:var(--ink);font-weight:900;font-size:38px;
    text-align:center;line-height:1.25;padding:6px 0;box-sizing:border-box;}
  .points__op{color:var(--white);font-weight:900;font-size:56px;line-height:1;height:56px;
    display:flex;align-items:center;-webkit-text-stroke:2px var(--ink);}
</style>
</head>
<body>
<div class="banner">
  <svg class="decor" width="1200" height="800" viewBox="0 0 1200 800" aria-hidden="true">
    <defs>
      <polygon id="burst" points="100,0 75.3,20.2 86.6,50 55.2,55.2 50,86.6 20.2,75.3 0,100 -20.2,75.3 -50,86.6 -55.2,55.2 -86.6,50 -75.3,20.2 -100,0 -75.3,-20.2 -86.6,-50 -55.2,-55.2 -50,-86.6 -20.2,-75.3 0,-100 20.2,-75.3 50,-86.6 55.2,-55.2 86.6,-50 75.3,-20.2"/>
    </defs>
    <use href="#burst" fill="var(--red)" transform="translate(250 470) rotate(8) scale(2.5 2.1)"/>
    <use href="#burst" fill="var(--yellow)" transform="translate(250 470) rotate(8) scale(2.2 1.82)"/>
  </svg>

  <div class="photo photo--truck-left" role="img" aria-label="白い中型トラックの写真"></div>
  <div class="photo photo--truck-right" role="img" aria-label="白い中型トラックの写真"></div>
  <div class="photo photo--crew" role="img" aria-label="作業着姿で笑顔のドライバー二人の写真"></div>

  <svg class="decor" width="1200" height="800" viewBox="0 0 1200 800" aria-hidden="true">
    <use href="#burst" fill="var(--red)" transform="translate(905 52) rotate(10) scale(0.5)"/>
  </svg>

  <h1 class="headline">6tドライバー募集!!</h1>

  <p class="salary-label">月給</p>
  <svg class="salary-figure" width="400" height="260" viewBox="0 0 400 260" role="img" aria-label="35">
    <defs>
      <linearGradient id="figureFill" x1="0" y1="0" x2="0" y2="1">
        <stop offset="0" stop-color="var(--blue-top)"/>
        <stop offset="1" stop-color="var(--blue-bottom)"/>
      </linearGradient>
    </defs>
    <text x="190" y="228" text-anchor="middle" font-family="Noto Sans JP, sans-serif" font-weight="900"
      font-size="290" letter-spacing="-8" fill="url(#figureFill)" stroke="var(--white)" stroke-width="14"
      paint-order="stroke" stroke-linejoin="round">35</text>
  </svg>
  <p class="salary-unit">万円可能</p>

  <ul class="points">
    <li class="points__item">固定ルート</li>
    <li class="points__op">＋</li>
    <li class="points__item">体力負担なし</li>
    <li class="points__op">＋</li>
    <li class="points__item">無理な運転は<br>させない社風</li>
    <li class="points__op">＝</li>
    <li class="points__item">長く働ける職場</li>
  </ul>
</div>
</body>
</html>
```